Roll-up display notepad needed for technology-oriented media production company

For a small convention, we need a rollup (85 cm x 200 cm) representing what we offer: media production (video, computer animation, web design, print) for scientifically and technically oriented businesses or organizations. So far, only the logo and a rough idea / layout exist (see attached.,. Png) how to combine bullet points, photographs (see the produced content, see: www.torvapex.com for inspiration with colors, pictures etc .), logo, web adress and so on. This sketch should be taken as a structural guide, it is quite ugly with regards to design, of course. This is where your task begins: Transforming this layout into something fresh. Additionally, we need paper notepads in DIN A7 as a giveway. The attached (only in German, sorry) respectively .ai templates for both the rollup and the notepad should help to deal with the borders / margins necessary for print. So, for additional version of the final vector data should be compatible with AI CS5. If you think you understand the look & amp; feel needed at the interface of science, education & amp; technology on the one hand and marketing on the other hand, we are happy to receive your design suggestions. Do not hesitate to ask questions to clarify the task, if necessary :) Kind regards!

```html
<!DOCTYPE html>
<html lang="en">
<head>
<meta charset="utf-8">
<title>Torvapex Notepad Page</title>
<link rel="stylesheet" href="https://fonts.googleapis.com/css2?family=Montserrat:wght@500;600;700&display=swap">
<style>
  :root {
    --backdrop: #ffffff;
    --page-light: #f8f8f9;
    --page-shade: #ececec;
    --accent-orange: #e35226;
    --band-black: #000000;
    --band-grey: #b8b8b8;
    --rule-line: #5a5a5a;
    --ink: #1e1e1e;
    --on-accent: #ffffff;
  }
  html, body {
    margin: 0;
    padding: 0;
    width: 1200px;
    height: 1200px;
    overflow: hidden;
    background: var(--backdrop);
  }
  .canvas {
    display: block;
    width: 1200px;
    height: 1200px;
  }
  .brand-name {
    font-family: "Montserrat", sans-serif;
    font-weight: 600;
    font-size: 34px;
    fill: var(--ink);
  }
  .brand-tagline {
    font-family: "Montserrat", sans-serif;
    font-weight: 500;
    font-size: 10.5px;
    fill: var(--ink);
  }
  .web-address {
    font-family: "Montserrat", sans-serif;
    font-weight: 700;
    font-size: 27px;
    fill: var(--on-accent);
  }
</style>
</head>
<body>
<svg class="canvas" viewBox="0 0 1500 1500" xmlns="http://www.w3.org/2000/svg">
  <defs>
    <linearGradient id="page-tone" x1="0" y1="1" x2="1" y2="0">
      <stop offset="0" stop-color="var(--page-light)"/>
      <stop offset="0.5" stop-color="var(--page-shade)"/>
      <stop offset="1" stop-color="var(--page-light)"/>
    </linearGradient>
  </defs>

  <g class="notepad-page">
    <rect class="page-sheet" x="73" y="313" width="1355" height="880" fill="url(#page-tone)"/>

    <g class="corner-bands corner-top-right">
      <polygon fill="var(--band-grey)" points="1020,313 1048,313 1280,487 1252,487"/>
      <polygon fill="var(--band-black)" points="1060,313 1095,313 1371,520 1336,520"/>
      <polygon fill="var(--accent-orange)" points="1110,313 1428,313 1428,552"/>
    </g>

    <g class="corner-bands corner-bottom-left">
      <polygon fill="var(--band-grey)" points="175,1070 355,1193 335,1193 160,1080"/>
      <polygon fill="var(--band-black)" points="138,1048 325,1193 300,1193 118,1060"/>
      <polygon fill="var(--accent-orange)" points="73,1055 290,1193 73,1193"/>
    </g>

    <g class="brand-block">
      <text class="brand-name" x="197" y="519">torvapex</text>
      <text class="brand-tagline" x="198" y="533">media | research | stories</text>
    </g>

    <g class="writing-lines" stroke="var(--rule-line)" stroke-width="2.5">
      <line x1="146" y1="569" x2="1354" y2="569"/>
      <line x1="146" y1="606" x2="1354" y2="606"/>
      <line x1="146" y1="644" x2="1354" y2="644"/>
      <line x1="146" y1="681" x2="1354" y2="681"/>
      <line x1="146" y1="718" x2="1354" y2="718"/>
      <line x1="146" y1="756" x2="1354" y2="756"/>
      <line x1="146" y1="793" x2="1354" y2="793"/>
      <line x1="146" y1="830" x2="1354" y2="830"/>
      <line x1="146" y1="867" x2="1354" y2="867"/>
      <line x1="146" y1="905" x2="1354" y2="905"/>
      <line x1="146" y1="942" x2="1354" y2="942"/>
      <line x1="146" y1="979" x2="1354" y2="979"/>
      <line x1="146" y1="1017" x2="1354" y2="1017"/>
    </g>

    <g class="web-pill">
      <rect x="970" y="1072" width="354" height="48" rx="24" fill="var(--accent-orange)"/>
      <text class="web-address" x="1147" y="1105" text-anchor="middle">www.torvapex.com</text>
    </g>
  </g>
</svg>
</body>
</html>
```